Floristry Business Card Design Project

I have a logo now and am looking to incorporate this into a business card. I would like a double sided business card. I would like one side to be decorative so that it blends well when included with floral arrangements and that can also be used as the front of a card and the other side will contain the business details. The font on the business details side should be clear although some decorative font would be ok. I have included the logo files for use in the business card design.

Feel free to break up the logo and use certain aspects of it in the design. Really looking for something that stands out and that is really creative.

Industry/Entity Type

Floral

Requirements
Should not have
• Nothing tacky or corny. The logo should be clearly read (perhaps a background colour).

```html
<!DOCTYPE html>
<html lang="en">
<head>
<meta charset="utf-8">
<title>Willow Meadow Business Card</title>
<link rel="stylesheet" href="https://fonts.googleapis.com/css2?family=Open+Sans:wght@400;600&display=swap">
<style>
  :root {
    --backdrop: #c9c9cb;
    --paper: #ffffff;
    --sage: #8fc3a0;
    --sage-deep: #6fae86;
    --sage-faint: #b4d9bf;
    --ink: #2b2b2b;
    --ink-soft: #555555;
    --white: #ffffff;
  }
  * { margin: 0; padding: 0; box-sizing: border-box; }
  html, body {
    width: 1200px;
    height: 900px;
    overflow: hidden;
    background: var(--backdrop);
    font-family: "Open Sans", Arial, sans-serif;
  }
  .canvas {
    width: 1200px;
    height: 900px;
    display: flex;
    align-items: center;
    justify-content: center;
    gap: 40px;
  }
  .card {
    position: relative;
    width: 560px;
    height: 320px;
    background: var(--paper);
    overflow: hidden;
    box-shadow: 0 2px 6px rgba(0,0,0,0.12);
  }

  /* Shared brand lockup */
  .brand {
    position: absolute;
    left: 50%;
    transform: translateX(-50%);
    display: flex;
    flex-direction: column;
    align-items: center;
  }
  .brand-mark {
    border-radius: 50%;
    border: 2px solid var(--sage);
  }
  .brand-name {
    font-family: "Open Sans", Arial, sans-serif;
    font-weight: 400;
    color: var(--sage-deep);
    text-transform: uppercase;
    letter-spacing: 4px;
    white-space: nowrap;
  }

  /* Decorative side */
  .card-front .brand { top: 92px; }
  .card-front .brand-mark { width: 82px; height: 82px; }
  .card-front .brand-name { margin-top: 10px; font-size: 13px; }
  .card-front .website {
    position: absolute;
    left: 0;
    right: 0;
    bottom: 48px;
    text-align: center;
    font-size: 14px;
    letter-spacing: 4px;
    color: var(--ink-soft);
  }

  /* Details side */
  .card-back .brand { top: 26px; }
  .card-back .brand-mark { width: 68px; height: 68px; }
  .card-back .brand-name { margin-top: 6px; font-size: 12px; }
  .card-back .address {
    position: absolute;
    top: 138px;
    left: 0;
    right: 0;
    text-align: center;
    font-size: 12.5px;
    color: var(--ink);
    padding-left: 120px;
  }
  .details-band {
    position: absolute;
    left: 0;
    right: 0;
    top: 162px;
    bottom: 0;
    background: var(--sage);
  }
  .contact {
    position: absolute;
    left: 26px;
    top: 14px;
    color: var(--white);
  }
  .contact-name {
    font-size: 17px;
    font-weight: 600;
    margin-bottom: 6px;
  }
  .contact-name .title {
    font-size: 12px;
    font-weight: 400;
    margin-left: 4px;
  }
  .contact-list { list-style: none; }
  .contact-list li {
    display: flex;
    align-items: center;
    gap: 7px;
    font-size: 12.5px;
    line-height: 21px;
  }
  .contact-list svg {
    width: 12px;
    height: 12px;
    fill: none;
    stroke: var(--white);
    stroke-width: 1.6;
  }
  .band-watermark {
    position: absolute;
    right: 28px;
    bottom: 26px;
    font-size: 30px;
    letter-spacing: 6px;
    text-transform: uppercase;
    color: var(--sage-faint);
    font-weight: 400;
  }
</style>
</head>
<body>
<main class="canvas">

  <section class="card card-front" aria-label="Decorative card side">
    <div class="brand">
      <div class="brand-mark" aria-hidden="true"></div>
      <div class="brand-name">Willow Meadow</div>
    </div>
    <p class="website">www.willowmeadow.com</p>
  </section>

  <section class="card card-back" aria-label="Business details card side">
    <div class="brand">
      <div class="brand-mark" aria-hidden="true"></div>
      <div class="brand-name">Willow Meadow</div>
    </div>
    <p class="address">Street Name, City Name, Zip Code-00000</p>

    <div class="details-band">
      <div class="contact">
        <p class="contact-name">Your Name,<span class="title">Title</span></p>
        <ul class="contact-list">
          <li>
            <svg viewBox="0 0 12 12" aria-hidden="true"><path d="M2.5 1.5 L4.5 1.5 L5.3 4 L4 5 Q5 7.2 7 8 L8 6.7 L10.5 7.5 L10.5 9.5 Q10.5 10.5 9.5 10.5 Q2 10 1.5 2.5 Q1.5 1.5 2.5 1.5 Z"/></svg>
            012-345-6789
          </li>
          <li>
            <svg viewBox="0 0 12 12" aria-hidden="true"><rect x="3" y="1" width="6" height="10" rx="1"/><line x1="5" y1="9" x2="7" y2="9"/></svg>
            012-345-6789
          </li>
          <li>
            <svg viewBox="0 0 12 12" aria-hidden="true"><rect x="1" y="2.5" width="10" height="7" rx="1"/><path d="M1 3 L6 6.8 L11 3"/></svg>
            admin@willowmeadow.com
          </li>
          <li>
            <svg viewBox="0 0 12 12" aria-hidden="true"><circle cx="6" cy="6" r="4.8"/><ellipse cx="6" cy="6" rx="2" ry="4.8"/><line x1="1.2" y1="6" x2="10.8" y2="6"/></svg>
            www.willowmeadow.com
          </li>
        </ul>
      </div>
      <div class="band-watermark" aria-hidden="true">Willow Meadow</div>
    </div>
  </section>

</main>
</body>
</html>
```